Business Card Design Project

Tall Pine Path- http:tallpinepath.com./rosalindkerr

Industry/Entity Type

Business

Contact Information for Business Card

Well it could be a pretty color like a glossy pink look business type very Job related

```html
<!DOCTYPE html>
<html lang="en">
<head>
<meta charset="utf-8">
<title>Rosalind Kerr — Business Card</title>
<link rel="stylesheet" href="https://fonts.googleapis.com/css2?family=Cinzel:wght@400;500&family=Open+Sans:wght@400&display=swap">
<style>
  :root {
    --stage: #e8e5e2;
    --charcoal: #333333;
    --pink: #ec1561;
    --paper: #ececec;
    --ink: #1f1f1f;
    --soft-white: #f2f2f2;
    --icon-tile: #e6e6e6;
  }
  * { margin: 0; padding: 0; box-sizing: border-box; }
  html, body { width: 1200px; height: 900px; overflow: hidden; }
  body { background: var(--stage); position: relative; }

  .card { position: absolute; box-shadow: 0 6px 18px rgba(0,0,0,.18); }

  /* Front: dark card */
  .card-front {
    left: 177px; top: 73px; width: 590px; height: 365px;
    background: var(--charcoal);
  }
  .front-name {
    position: absolute; left: 30px; top: 58px;
    font-family: "Cinzel", serif; font-weight: 500;
    font-size: 21px; letter-spacing: .5px; color: var(--pink);
  }
  .contact-list {
    position: absolute; left: 31px; top: 117px; list-style: none;
    font-family: "Open Sans", sans-serif; font-size: 15.5px; color: var(--soft-white);
  }
  .contact-item { display: flex; align-items: center; height: 21.5px; }
  .contact-icon { width: 13px; height: 13px; margin-right: 7px; fill: var(--pink); }
  .follow-label {
    position: absolute; left: 30px; top: 260px;
    font-family: "Cinzel", serif; font-size: 13px; letter-spacing: .8px; color: var(--soft-white);
  }
  .social-row { position: absolute; left: 30px; top: 289px; display: flex; gap: 9px; }
  .social-tile { width: 24px; height: 24px; background: var(--icon-tile); }

  .brand-panel {
    position: absolute; left: 310px; top: 0; width: 280px; height: 365px;
    border: 7px solid var(--pink); border-right: none;
    display: flex; flex-direction: column; align-items: center; justify-content: center; gap: 18px;
  }
  .brand-square { width: 70px; height: 70px; border: 7px solid var(--pink); }
  .brand-name {
    font-family: "Cinzel", serif; font-weight: 500; font-size: 26px;
    line-height: 1.25; text-align: center; color: var(--pink);
  }

  /* Back: light card */
  .card-back {
    left: 388px; top: 505px; width: 566px; height: 352px;
    background: var(--paper);
  }
  .back-mark {
    position: absolute; left: 220px; top: 95px; width: 128px; height: 113px;
    border: 5px solid var(--pink);
  }
  .back-name {
    position: absolute; left: 0; right: 0; top: 222px; text-align: center;
    font-family: "Cinzel", serif; font-size: 34px; color: var(--ink); letter-spacing: .3px;
  }
</style>
</head>
<body>
  <section class="card card-front">
    <h1 class="front-name">ROSALIND KERR</h1>
    <ul class="contact-list">
      <li class="contact-item">
        <svg class="contact-icon" viewBox="0 0 16 16"><path d="M3.6 1.2l2.3 2.6-1.3 1.9c.9 2 2.6 3.7 4.6 4.6l1.9-1.3 2.6 2.3-1.3 2.4C7.3 14 2 8.7 1.3 3.8z"/></svg>
        (044)987650432
      </li>
      <li class="contact-item">
        <svg class="contact-icon" viewBox="0 0 16 16"><path d="M1 3h14v1.2L8 9 1 4.2z"/><path d="M1 5.8l7 4.8 7-4.8V13H1z"/></svg>
        info@tallpinepath.com
      </li>
      <li class="contact-item">
        <svg class="contact-icon" viewBox="0 0 16 16"><circle cx="8" cy="8" r="6.5"/></svg>
        www.tallpinepath.com
      </li>
    </ul>
    <p class="follow-label">FOLLOW US ON</p>
    <div class="social-row">
      <span class="social-tile"></span>
      <span class="social-tile"></span>
      <span class="social-tile"></span>
      <span class="social-tile"></span>
    </div>
    <div class="brand-panel">
      <span class="brand-square"></span>
      <span class="brand-name">Rosalind<br>Kerr</span>
    </div>
  </section>

  <section class="card card-back">
    <span class="back-mark"></span>
    <h2 class="back-name">Rosalind Kerr</h2>
  </section>
</body>
</html>
```